Website for software company "velbra"

We need a website for our software company/startup named "velbra". We are developing several products (currently 3 standard-software products) which are all in different sectors, but all our products are available for Laptops/PC/Mobile Phones/Tablets, ... We do also create custom software and support our customers with consulting to optimize their processes.
We already have a Logo which you can find in the attached files.
We are a young team of 4 members (two founders and 2 employees).

To get an idea of our products -> the first one is a planning software for healthcare organizations (eg. Mercyway, firebrigade, pharmacy), the second one is a booking software for sport clubs and the third one is a competition software for sports hunting. You see very diverse. Include or ignore this info of our products as you like.

The design has to be a bootstrap 4 (or higher) design. We have licenced FontAwesome as iconset. Responsive design should come without saying.

Coding

Coded - Design and coding required

Number of Pages Required

5+ page

Font styles to use
Sans Serif

Requirements
Must have
• Starting page, product pages, news section, contact, team, services

```html
<!DOCTYPE html>
<html lang="en">
<head>
<meta charset="utf-8">
<title>velbra — Software Products</title>
<link rel="stylesheet" href="https://fonts.googleapis.com/css2?family=Outfit:wght@300;400;500;600;700&display=swap">
<style>
:root{
  --orange:#f47f32;
  --orange-dark:#e06d22;
  --navy:#263040;
  --navy-deep:#1c2430;
  --ink:#1f2733;
  --text:#4a4f57;
  --muted:#8a8f97;
  --white:#ffffff;
  --field:#3a4454;
}
*{box-sizing:border-box;margin:0;padding:0}
html,body{width:1200px;height:4254px;overflow:hidden}
body{position:relative;font-family:"Outfit",Arial,sans-serif;color:var(--ink);background:var(--white)}
a{text-decoration:none;color:inherit}
.abs{position:absolute}

/* buttons */
.btn{position:absolute;display:flex;align-items:center;justify-content:center;gap:9px;border-radius:30px;font-weight:600;color:var(--white);background:var(--orange)}
.btn svg{flex:none}
.btn--dark{background:var(--navy)}

/* header */
.site-header{position:absolute;left:0;top:0;width:1200px;height:118px;z-index:3}
.brand{position:absolute;display:flex;align-items:center;gap:10px;font-weight:700;color:var(--ink)}
.brand__mark{width:24px;height:24px;background:var(--orange)}
.site-header .brand{left:172px;top:22px;font-size:44px;letter-spacing:1px}
.main-nav{position:absolute;left:398px;top:27px;display:flex;gap:0}
.main-nav a{font-size:14px;color:var(--ink);margin-right:31px}
.main-nav a.is-active{color:var(--orange)}
.phone-pill{position:absolute;left:849px;top:15px;width:177px;height:42px;background:var(--navy);border-radius:22px;display:flex;align-items:center;color:#fff;font-weight:600;font-size:16px;padding-left:4px;gap:10px}
.phone-pill__icon{width:34px;height:34px;border-radius:50%;background:#fff;display:flex;align-items:center;justify-content:center}

/* hero */
.hero-art{position:absolute;left:0;top:0;width:1200px;height:590px}
.hero__title{position:absolute;left:173px;top:213px;font-size:46px;line-height:54px;font-weight:700;color:#fff}
.hero__sub{position:absolute;left:173px;top:335px;font-size:19px;color:#fff;font-weight:400}
.hero .btn{left:173px;top:376px;width:179px;height:53px;font-size:16px}

/* welcome */
.welcome__kicker{position:absolute;left:184px;top:690px;font-size:33px;font-weight:400;color:var(--ink);display:flex;align-items:center;gap:10px}
.welcome__kicker i{display:inline-block;width:20px;height:20px;background:var(--orange)}
.welcome__name{position:absolute;left:184px;top:726px;font-size:58px;font-weight:600;letter-spacing:3px;color:var(--ink)}
.welcome__text{position:absolute;left:459px;top:664px;width:575px;font-size:20.5px;line-height:31px;color:var(--text);font-weight:300}
.welcome .btn{left:459px;top:811px;width:178px;height:53px;font-size:17px}

/* section heading */
.section-title{position:absolute;left:0;width:1200px;text-align:center;font-size:40px;font-weight:600;color:var(--ink)}
.section-title span{color:var(--orange);font-weight:400}
.section-title--light{color:#fff}
.section-mark{position:absolute;left:592px;width:16px;height:16px;background:var(--orange)}

/* bands */
.band{position:absolute;left:0;width:1200px}
.band svg{position:absolute;left:0;top:0}

/* products */
.product-card{position:absolute;top:1164px;width:259px;height:385px;border:3px solid var(--orange);border-radius:130px 130px 115px 115px;padding:9px}
.product-card__inner{position:relative;width:100%;height:100%;background:#fff;border-radius:120px 120px 105px 105px;overflow:hidden;text-align:center}
.product-card__top{position:absolute;left:0;top:0;width:100%;height:150px;background:var(--orange);border-radius:0 0 50% 50%/0 0 48px 48px}
.product-card__icon{position:absolute;left:50%;top:52px;width:64px;height:64px;margin-left:-32px;border:3px solid rgba(255,255,255,.85);border-radius:12px}
.product-card h3{position:absolute;left:0;top:168px;width:100%;font-size:20px;line-height:24px;font-weight:600;color:var(--ink)}
.product-card p{position:absolute;left:18px;top:222px;width:205px;font-size:16.5px;line-height:25px;color:var(--text);font-weight:300}
.product-card .link{position:absolute;left:0;top:303px;width:100%;display:flex;justify-content:center;align-items:center;gap:7px;color:var(--orange);font-weight:600;font-size:17px}

/* services */
.service-card{position:absolute;top:1808px;width:268px;height:363px;background:#fff;box-shadow:0 6px 22px rgba(0,0,0,.1)}
.service-card__media{width:268px;height:175px}
.service-card h3{position:absolute;left:20px;top:195px;font-size:20px;font-weight:500;color:var(--ink)}
.service-card p{position:absolute;left:20px;top:229px;width:232px;font-size:14.5px;line-height:22px;color:var(--text);font-weight:300}
.service-card .btn{left:20px;top:306px;width:127px;height:37px;font-size:13.5px;gap:7px}

/* team */
.member{position:absolute;top:2415px;width:200px;margin-left:-100px;text-align:center}
.member__ring{position:relative;width:198px;height:198px;margin:0 auto}
.member__ring svg{position:absolute;left:0;top:0}
.member__photo{position:absolute;left:20px;top:20px;width:158px;height:158px;border-radius:50%}
.member h4{margin-top:17px;font-size:17px;font-weight:600;color:#fff}
.member small{display:block;margin-top:3px;font-size:13px;font-style:italic;color:#9aa2ad;font-weight:300}

/* news */
.news-card{position:absolute;top:2937px;width:268px}
.news-card__media{position:relative;width:268px;height:185px}
.news-card__date{position:absolute;left:15px;bottom:-6px;background:var(--orange);color:#fff;font-size:12.5px;font-weight:500;padding:4px 12px}
.news-card h3{margin-top:20px;font-size:19px;font-weight:500;color:var(--ink)}
.news-card p{margin-top:8px;font-size:14.5px;line-height:22px;color:var(--text);font-weight:300}
.news-card .btn{position:relative;margin-top:16px;width:127px;height:37px;font-size:13.5px;gap:7px}
.slider-arrow{position:absolute;top:3006px;width:48px;height:47px;display:flex;align-items:center;justify-content:center}
.slider-arrow--prev{left:150px;background:#3b3f45}
.slider-arrow--next{left:1007px;background:var(--orange)}

/* contact */
.contact-field{position:absolute;height:38px;background:var(--field);border:1px solid #5d6676;color:#d6dae0;font-size:14px;padding:9px 12px;font-family:inherit}
.contact-form .btn{left:525px;top:3758px;width:149px;height:46px;font-size:17px}

/* footer */
.site-footer .brand{left:172px;top:4002px;font-size:50px}
.socials{position:absolute;left:196px;top:4079px;display:flex;gap:12px}
.socials span{width:34px;height:34px;border-radius:50%;background:#e9eaec;display:flex;align-items:center;justify-content:center}
.socials span i{width:12px;height:12px;border-radius:50%;background:#555b63}
.copyright{position:absolute;left:190px;top:4166px;font-size:12px;color:#666}
.copyright b{color:var(--orange);font-weight:400}
.footer-col{position:absolute;top:3981px}
.footer-col h5{font-size:14px;font-weight:500;color:var(--orange);letter-spacing:.5px;margin-bottom:14px}
.footer-col ul{list-style:none}
.footer-col li{position:relative;font-size:14px;line-height:20px;color:#333;padding-left:16px;margin-bottom:14px;font-weight:300}
.footer-col li::before{content:"";position:absolute;left:2px;top:6px;border-left:5px solid var(--orange);border-top:4px solid transparent;border-bottom:4px solid transparent}
.footer-col--contact li{padding-left:24px}
.footer-col--contact li::before{display:none}
.footer-col--contact svg{position:absolute;left:0;top:3px}
</style>
</head>
<body>

<!-- HERO -->
<section class="hero">
  <svg class="hero-art" width="1200" height="590" viewBox="0 0 1200 590" role="img" aria-label="Photo of a businessman working at a desk, tinted orange">
    <defs>
      <linearGradient id="heroTint" x1="0" y1="0" x2="1" y2="1">
        <stop offset="0" stop-color="#f08a45"/>
        <stop offset=".55" stop-color="#e47a36"/>
        <stop offset="1" stop-color="#c9652a"/>
      </linearGradient>
    </defs>
    <polygon points="0,118 360,118 405,72 1200,72 1200,553 510,553 463,590 0,590" fill="url(#heroTint)"/>
    <polygon points="620,130 1130,130 1130,500 620,500" fill="#b35a26" opacity=".35"/>
  </svg>
  <h1 class="hero__title">We are Developing<br>Several Products</h1>
  <p class="hero__sub">Which are all in different sectors</p>
  <a class="btn btn--dark" href="#">Know More
    <svg width="18" height="18" viewBox="0 0 18 18"><circle cx="9" cy="9" r="9" fill="#fff"/><path d="M5 9h7M9 5.5L12.5 9 9 12.5" stroke="#263040" stroke-width="2" fill="none"/></svg>
  </a>
</section>

<!-- HEADER -->
<header class="site-header">
  <a class="brand" href="#"><span class="brand__mark"></span>velbra</a>
  <nav class="main-nav">
    <a class="is-active" href="#">Home</a><a href="#">Product</a><a href="#">News</a><a href="#">Team</a><a href="#">Services</a><a href="#">Contact</a>
  </nav>
  <a class="phone-pill" href="#">
    <span class="phone-pill__icon"><svg width="18" height="18" viewBox="0 0 24 24"><path d="M6.6 10.8a15 15 0 006.6 6.6l2.2-2.2a1 1 0 011-.25 11.4 11.4 0 003.6.57 1 1 0 011 1V20a1 1 0 01-1 1A17 17 0 013 4a1 1 0 011-1h3.5a1 1 0 011 1 11.4 11.4 0 00.57 3.6 1 1 0 01-.25 1z" fill="#f47f32"/></svg></span>
    01 555 246 810
  </a>
</header>

<!-- WELCOME -->
<section class="welcome">
  <p class="welcome__kicker">Welcome to <i></i></p>
  <h2 class="welcome__name">VELBRA</h2>
  <p class="welcome__text">Lorem ipsum dolor sit amet, consectetur adipiscing elit, sed do eiusmod tempor incididunt ut labore et dolore magna aliqua. Quis ipsum suspendisse ultes graa. Risus commodo viverra maecenas accumsan lacus vel facilisis.</p>
  <a class="btn" href="#">Read More
    <svg width="19" height="19" viewBox="0 0 18 18"><circle cx="9" cy="9" r="9" fill="#fff"/><path d="M5 9h7M9 5.5L12.5 9 9 12.5" stroke="#f47f32" stroke-width="2" fill="none"/></svg>
  </a>
</section>

<!-- PRODUCTS -->
<section class="band products" style="top:987px;height:672px">
  <svg width="1200" height="672" viewBox="0 0 1200 672">
    <polygon points="0,45 360,45 405,0 1200,0 1200,625 500,625 455,672 0,672" fill="#263040"/>
    <polyline points="0,63 363,63 415,12 1200,12" fill="none" stroke="#f47f32" stroke-width="4"/>
    <polyline points="1200,617 495,617 447,662 0,662" fill="none" stroke="#f47f32" stroke-width="4"/>
  </svg>
</section>
<h2 class="section-title section-title--light" style="top:1052px"><span>Our</span> Product</h2>
<span class="section-mark" style="top:1110px"></span>

<article class="product-card" style="left:173px">
  <div class="product-card__inner">
    <div class="product-card__top"><span class="product-card__icon" role="img" aria-label="Healthcare monitor icon"></span></div>
    <h3>Healthcare<br>Organizations</h3>
    <p>Risus commodo viverra maecenas accumsan lacus vel facilisis.</p>
    <a class="link" href="#">View Details <svg width="16" height="16" viewBox="0 0 18 18"><circle cx="9" cy="9" r="9" fill="#f47f32"/><path d="M5 9h7M9 5.5L12.5 9 9 12.5" stroke="#fff" stroke-width="2" fill="none"/></svg></a>
  </div>
</article>
<article class="product-card" style="left:470px">
  <div class="product-card__inner">
    <div class="product-card__top"><span class="product-card__icon" role="img" aria-label="Booking settings icon"></span></div>
    <h3>Booking software<br>For sport clubs</h3>
    <p>Risus commodo viverra maecenas accumsan lacus vel facilisis.</p>
    <a class="link" href="#">View Details <svg width="16" height="16" viewBox="0 0 18 18"><circle cx="9" cy="9" r="9" fill="#f47f32"/><path d="M5 9h7M9 5.5L12.5 9 9 12.5" stroke="#fff" stroke-width="2" fill="none"/></svg></a>
  </div>
</article>
<article class="product-card" style="left:768px">
  <div class="product-card__inner">
    <div class="product-card__top"><span class="product-card__icon" role="img" aria-label="Sports balls icon"></span></div>
    <h3>Competition Software<br>For sports hunting</h3>
    <p>Risus commodo viverra maecenas accumsan lacus vel facilisis,</p>
    <a class="link" href="#">View Details <svg width="16" height="16" viewBox="0 0 18 18"><circle cx="9" cy="9" r="9" fill="#f47f32"/><path d="M5 9h7M9 5.5L12.5 9 9 12.5" stroke="#fff" stroke-width="2" fill="none"/></svg></a>
  </div>
</article>

<!-- SERVICES -->
<h2 class="section-title" style="top:1716px"><span>Our</span> Services</h2>
<span class="section-mark" style="top:1774px"></span>

<article class="service-card" style="left:173px">
  <div class="service-card__media" role="img" aria-label="Photo of hands typing on a laptop" style="background:linear-gradient(135deg,#c9ced4,#8c939b 60%,#5a6068)"></div>
  <h3>Vestibulum viverra</h3>
  <p>Vivamus et velit a odio semper blandit eu eget odio. Duis non bibendum urna. Morbi lacinia,</p>
  <a class="btn" href="#">Read More <svg width="13" height="13" viewBox="0 0 18 18"><circle cx="9" cy="9" r="9" fill="#fff"/><path d="M5 9h7M9 5.5L12.5 9 9 12.5" stroke="#f47f32" stroke-width="2.4" fill="none"/></svg></a>
</article>
<article class="service-card" style="left:466px">
  <div class="service-card__media" role="img" aria-label="Photo of a developer working at a computer" style="background:linear-gradient(135deg,#e4e2dc,#a7a39a 55%,#5c6872)"></div>
  <h3>Vestibulum viverra</h3>
  <p>Vivamus et velit a odio semper blandit eu eget odio. Duis non bibendum urna. Morbi lacinia,</p>
  <a class="btn" href="#">Read More <svg width="13" height="13" viewBox="0 0 18 18"><circle cx="9" cy="9" r="9" fill="#fff"/><path d="M5 9h7M9 5.5L12.5 9 9 12.5" stroke="#f47f32" stroke-width="2.4" fill="none"/></svg></a>
</article>
<article class="service-card" style="left:759px">
  <div class="service-card__media" role="img" aria-label="Photo of a consultant in an office" style="background:linear-gradient(135deg,#d8d0b8,#a9b7c7 55%,#4f73a6)"></div>
  <h3>Vestibulum viverra</h3>
  <p>Vivamus et velit a odio semper blandit eu eget odio. Duis non bibendum urna. Morbi lacinia,</p>
  <a class="btn" href="#">Read More <svg width="13" height="13" viewBox="0 0 18 18"><circle cx="9" cy="9" r="9" fill="#fff"/><path d="M5 9h7M9 5.5L12.5 9 9 12.5" stroke="#f47f32" stroke-width="2.4" fill="none"/></svg></a>
</article>

<!-- TEAM -->
<section class="band team" style="top:2240px;height:555px">
  <svg width="1200" height="555" viewBox="0 0 1200 555" role="img" aria-label="Dark blue office background photo">
    <defs>
      <linearGradient id="teamBg" x1="0" y1="0" x2="1" y2="1">
        <stop offset="0" stop-color="#1a2231"/><stop offset=".5" stop-color="#223049"/><stop offset="1" stop-color="#161d2a"/>
      </linearGradient>
    </defs>
    <polygon points="0,45 360,45 405,0 1200,0 1200,508 500,508 455,555 0,555" fill="url(#teamBg)"/>
    <polyline points="0,63 363,63 415,12 1200,12" fill="none" stroke="#f47f32" stroke-width="4"/>
    <polyline points="1200,500 495,500 447,545 0,545" fill="none" stroke="#f47f32" stroke-width="4"/>
  </svg>
</section>
<h2 class="section-title section-title--light" style="top:2315px"><span>Our</span> Team Mamber</h2>
<span class="section-mark" style="top:2372px"></span>

<div class="member" style="left:272px">
  <div class="member__ring"><svg width="198" height="198"><circle cx="99" cy="99" r="93" fill="none" stroke="#f47f32" stroke-width="10" stroke-dasharray="2.5 4.5"/></svg>
  <div class="member__photo" role="img" aria-label="Portrait of a founder" style="background:linear-gradient(160deg,#f2f2f2,#c9ccd0)"></div></div>
  <h4>Lorem ipsum</h4><small>Founders</small>
</div>
<div class="member" style="left:490px">
  <div class="member__ring"><svg width="198" height="198"><circle cx="99" cy="99" r="93" fill="none" stroke="#f47f32" stroke-width="10" stroke-dasharray="2.5 4.5"/></svg>
  <div class="member__photo" role="img" aria-label="Portrait of a founder" style="background:linear-gradient(160deg,#f4f1ee,#d4c8bd)"></div></div>
  <h4>Lorem ipsum</h4><small>Founders</small>
</div>
<div class="member" style="left:708px">
  <div class="member__ring"><svg width="198" height="198"><circle cx="99" cy="99" r="93" fill="none" stroke="#f47f32" stroke-width="10" stroke-dasharray="2.5 4.5"/></svg>
  <div class="member__photo" role="img" aria-label="Portrait of an employee" style="background:linear-gradient(160deg,#eef0f3,#8e98a8)"></div></div>
  <h4>Lorem ipsum</h4><small>Employee</small>
</div>
<div class="member" style="left:926px">
  <div class="member__ring"><svg width="198" height="198"><circle cx="99" cy="99" r="93" fill="none" stroke="#f47f32" stroke-width="10" stroke-dasharray="2.5 4.5"/></svg>
  <div class="member__photo" role="img" aria-label="Portrait of an employee" style="background:linear-gradient(160deg,#f6f6f6,#b9bbbe)"></div></div>
  <h4>Lorem ipsum</h4><small>Employee</small>
</div>

<!-- NEWS -->
<h2 class="section-title" style="top:2841px"><span>Latest</span> News</h2>
<span class="section-mark" style="top:2898px"></span>

<article class="news-card" style="left:173px">
  <div class="news-card__media" role="img" aria-label="Photo of a man working on a laptop by a window" style="background:linear-gradient(135deg,#b7c7d3,#e4eaee 55%,#8fa3b3)"><span class="news-card__date">April 16, 2022</span></div>
  <h3>Vivamus et velit a odio</h3>
  <p>Donec cursus dapibus fermentum. Proin auctor diam maximus, hendrerit libero sit amet, porta nulla.</p>
  <a class="btn" href="#">Read More <svg width="13" height="13" viewBox="0 0 18 18"><circle cx="9" cy="9" r="9" fill="#fff"/><path d="M5 9h7M9 5.5L12.5 9 9 12.5" stroke="#f47f32" stroke-width="2.4" fill="none"/></svg></a>
</article>
<article class="news-card" style="left:466px">
  <div class="news-card__media" role="img" aria-label="Photo of a hand holding a smartphone showing a download screen" style="background:linear-gradient(135deg,#8a7d6d,#3fae86 50%,#5a4f44)"><span class="news-card__date">April 16, 2022</span></div>
  <h3>Vivamus et velit a odio</h3>
  <p>Donec cursus dapibus fermentum. Proin auctor diam maximus, hendrerit libero sit amet, porta nulla.</p>
  <a class="btn" href="#">Read More <svg width="13" height="13" viewBox="0 0 18 18"><circle cx="9" cy="9" r="9" fill="#fff"/><path d="M5 9h7M9 5.5L12.5 9 9 12.5" stroke="#f47f32" stroke-width="2.4" fill="none"/></svg></a>
</article>
<article class="news-card" style="left:759px">
  <div class="news-card__media" role="img" aria-label="Photo of a happy man holding a tablet" style="background:linear-gradient(135deg,#f4f4f4,#eed9d6 55%,#d9d9d9)"><span class="news-card__date">April 16, 2022</span></div>
  <h3>Vivamus et velit a odio</h3>
  <p>Donec cursus dapibus fermentum. Proin auctor diam maximus, hendrerit libero sit amet, porta nulla.</p>
  <a class="btn" href="#">Read More <svg width="13" height="13" viewBox="0 0 18 18"><circle cx="9" cy="9" r="9" fill="#fff"/><path d="M5 9h7M9 5.5L12.5 9 9 12.5" stroke="#f47f32" stroke-width="2.4" fill="none"/></svg></a>
</article>
<a class="slider-arrow slider-arrow--prev" href="#" aria-label="Previous"><svg width="14" height="24"><path d="M12 2L2 12l10 10" stroke="#fff" stroke-width="1.6" fill="none"/></svg></a>
<a class="slider-arrow slider-arrow--next" href="#" aria-label="Next"><svg width="14" height="24"><path d="M2 2l10 10L2 22" stroke="#fff" stroke-width="1.6" fill="none"/></svg></a>

<!-- CONTACT -->
<section class="band contact" style="top:3373px;height:565px">
  <svg width="1200" height="565" viewBox="0 0 1200 565" role="img" aria-label="Dark office background photo">
    <defs>
      <linearGradient id="contactBg" x1="0" y1="0" x2="1" y2="1">
        <stop offset="0" stop-color="#1f2837"/><stop offset=".5" stop-color="#2a3446"/><stop offset="1" stop-color="#1a212d"/>
      </linearGradient>
    </defs>
    <polygon points="0,45 360,45 405,0 1200,0 1200,518 500,518 455,565 0,565" fill="url(#contactBg)"/>
    <polyline points="0,63 363,63 415,12 1200,12" fill="none" stroke="#f47f32" stroke-width="4"/>
    <polyline points="1200,510 495,510 447,555 0,555" fill="none" stroke="#f47f32" stroke-width="4"/>
  </svg>
</section>
<h2 class="section-title section-title--light" style="top:3462px"><span>Get In</span> Touch</h2>
<span class="section-mark" style="top:3519px"></span>
<form class="contact-form">
  <div class="contact-field" style="left:234px;top:3560px;width:238px">Full Name</div>
  <div class="contact-field" style="left:479px;top:3560px;width:238px">Email</div>
  <div class="contact-field" style="left:725px;top:3560px;width:240px">Phone</div>
  <div class="contact-field" style="left:234px;top:3609px;width:731px;height:126px">Your Message</div>
  <a class="btn" href="#">Submit <svg width="17" height="17" viewBox="0 0 18 18"><circle cx="9" cy="9" r="9" fill="#fff"/><path d="M5 9h7M9 5.5L12.5 9 9 12.5" stroke="#f47f32" stroke-width="2" fill="none"/></svg></a>
</form>

<!-- FOOTER -->
<footer class="site-footer">
  <a class="brand" href="#"><span class="brand__mark"></span>velbra</a>
  <div class="socials"><span><i></i></span><span><i></i></span><span><i></i></span><span><i></i></span></div>
  <p class="copyright">© 2022 <b>velbra</b>. All right reserved</p>

  <div class="footer-col" style="left:429px">
    <h5>QUCIK LINKS</h5>
    <ul><li>Home</li><li>Product</li><li>News</li><li>Team</li><li>Services</li><li>Contact</li></ul>
  </div>
  <div class="footer-col" style="left:568px;width:220px">
    <h5>PRODUCT</h5>
    <ul><li>Healthcare Organizations</li><li>Booking software For sport clubs</li><li>Competition Software For sports hunting</li></ul>
  </div>
  <div class="footer-col footer-col--contact" style="left:819px;width:220px">
    <h5>CONTACT INFO</h5>
    <ul>
      <li><svg width="12" height="15" viewBox="0 0 12 15"><path d="M6 0a6 6 0 016 6c0 4-6 9-6 9S0 10 0 6a6 6 0 016-6z" fill="#f47f32"/><circle cx="6" cy="6" r="2.2" fill="#fff"/></svg>12 Harbour Lane, Sydney, Australia</li>
      <li><svg width="13" height="13" viewBox="0 0 24 24"><path d="M6.6 10.8a15 15 0 006.6 6.6l2.2-2.2a1 1 0 011-.25 11.4 11.4 0 003.6.57 1 1 0 011 1V20a1 1 0 01-1 1A17 17 0 013 4a1 1 0 011-1h3.5a1 1 0 011 1 11.4 11.4 0 00.57 3.6 1 1 0 01-.25 1z" fill="#f47f32"/></svg>01 555 7788 90</li>
      <li><svg width="13" height="10" viewBox="0 0 13 10"><rect width="13" height="10" rx="1" fill="#f47f32"/><path d="M1 1l5.5 4.5L12 1" stroke="#fff" stroke-width="1.2" fill="none"/></svg>hello@velbra.io</li>
    </ul>
  </div>
</footer>

</body>
</html>
```